professional business card design

Business card design. Photos have been uploaded and i am open to the designer choosing which photos to use. Would like the card to be mostyly in a grey scale design with black, whites, silver & grey colours. I have added copy of our flyer as would like on the back side of card our services to be listed. Do not use any bright colurs such as blue red green or yellow. i need to be able to edit the phone number and naem in the final card design submitted.

Target Market(s)

Clients

Industry/Entity Type

earhmovibng and transport

Contact Information for Business Card

Director Name, address, email, phone number and services

Colors

Designer to choose only greyscale colors for use in the design.

Requirements
Should not have
• no yellow, red, blue or green

```html
<!DOCTYPE html>
<html lang="en">
<head>
<meta charset="utf-8">
<title>Karrow Haulage Business Card</title>
<link href="https://fonts.googleapis.com/css2?family=Source+Sans+3:wght@400;600&family=Tinos&family=Kalam:wght@700&display=swap" rel="stylesheet">
<style>
  :root {
    --backdrop: #9a9c9b;
    --card: #0d0d0d;
    --card-edge: #1c1c1c;
    --accent: #6a6d71;
    --accent-text: #b4b7ba;
    --text: #f2f2f2;
    --silver: #d4d6d8;
    --earth: #7a7470;
  }
  * { margin: 0; padding: 0; box-sizing: border-box; }
  html, body { width: 1200px; height: 1200px; overflow: hidden; background: var(--backdrop); }
  .sheet { position: relative; width: 1200px; height: 1200px; }
  .card {
    position: absolute; left: 231px; width: 736px; height: 452px; overflow: hidden;
    background: radial-gradient(ellipse at 40% 50%, var(--card-edge), var(--card) 75%);
    color: var(--text); font-family: "Source Sans 3", sans-serif;
  }
  .card--front { top: 116px; }
  .card--back { top: 631px; }
  .abs { position: absolute; }

  .hero-photo {
    left: 0; top: 0; width: 736px; height: 294px;
    background: linear-gradient(180deg, #0b0b0b 0%, #151515 45%, #333 62%, var(--earth) 82%, #5e5955 100%);
  }
  .wordmark {
    left: 0; top: 36px; width: 736px; text-align: center;
    font-family: "Source Sans 3", sans-serif; font-weight: 600; font-size: 72px;
    letter-spacing: 6px; color: var(--silver); line-height: 1;
  }
  .chrome-rule {
    left: 0; top: 295px; width: 736px; height: 14px;
    background: linear-gradient(90deg, #0d0d0d 20%, #777 50%, #fff 62%, #777 75%, #0d0d0d 95%);
  }
  .company-tab {
    left: 0; top: 312px; height: 36px; background: var(--accent);
    border-radius: 0 4px 4px 0; padding: 0 12px 0 39px;
    font-size: 29px; font-weight: 600; line-height: 36px; color: #fff; white-space: nowrap;
  }
  .person-name { left: 39px; top: 354px; font-size: 31px; line-height: 1; }
  .person-role { left: 40px; top: 392px; font-size: 20px; color: var(--accent-text); line-height: 1; }
  .contact { right: 40px; top: 344px; text-align: right; font-size: 17px; line-height: 24px; }
  .contact li { list-style: none; display: flex; justify-content: flex-end; align-items: center; gap: 8px; }
  .contact svg { width: 14px; height: 14px; }

  .services-pill {
    left: 40px; top: 42px; width: 219px; height: 32px; background: var(--accent);
    border-radius: 8px; text-align: center;
    font-family: "Kalam", cursive; font-weight: 700; font-size: 24px; line-height: 34px;
    letter-spacing: 1.5px; color: #fff;
  }
  .service-list { font-family: "Tinos", serif; font-size: 21px; list-style: none; }
  .service-list li { position: relative; padding-left: 18px; height: 28px; line-height: 28px; white-space: nowrap; }
  .service-list li::before {
    content: ""; position: absolute; left: 0; top: 12px; width: 7px; height: 7px;
    border-radius: 50%; background: var(--accent-text);
  }
  .service-list--main { left: 43px; top: 99px; }
  .service-list--main li:nth-child(3) { margin-top: 2px; }
  .service-list--extra { left: 493px; top: 99px; }
  .service-list--extra li:nth-child(2) { margin-top: 2px; }
  .accent-bar { left: 0; top: 313px; width: 25px; height: 96px; background: var(--accent); border-radius: 0 5px 5px 0; }
  .pitch { left: 39px; top: 313px; width: 360px; font-family: "Kalam", cursive; font-weight: 700; font-size: 17px; line-height: 23px; }
  .depot { left: 39px; top: 388px; font-size: 17px; white-space: nowrap; }
  .depot span { color: var(--accent-text); }
  .truck-photo {
    left: 421px; top: 253px; width: 315px; height: 199px;
    background: radial-gradient(ellipse at 55% 55%, #9aa2a8 0%, #5f6468 40%, #2a2a2a 65%, transparent 75%);
  }
</style>
</head>
<body>
<main class="sheet">
  <section class="card card--front">
    <div class="abs hero-photo" role="img" aria-label="Road train with three dark tipper trailers on an outback dirt road at dusk"></div>
    <div class="abs wordmark">KARROW</div>
    <div class="abs chrome-rule"></div>
    <div class="abs company-tab">Karrow Haulage</div>
    <div class="abs person-name">MASON TULL</div>
    <div class="abs person-role">Director</div>
    <ul class="abs contact">
      <li>08 5550 1472
        <svg viewBox="0 0 24 24"><path fill="var(--accent-text)" d="M6.6 10.8a15 15 0 0 0 6.6 6.6l2.2-2.2a1 1 0 0 1 1-.25 11.4 11.4 0 0 0 3.6.6 1 1 0 0 1 1 1V20a1 1 0 0 1-1 1A17 17 0 0 1 3 4a1 1 0 0 1 1-1h3.5a1 1 0 0 1 1 1c0 1.25.2 2.45.6 3.6a1 1 0 0 1-.25 1z"/></svg></li>
      <li>office@karrowhaul.com
        <svg viewBox="0 0 24 24"><rect x="2" y="5" width="20" height="14" rx="1" fill="var(--accent-text)"/><path d="M2 6l10 7 10-7" stroke="#111" stroke-width="2" fill="none"/></svg></li>
      <li>karrowhaul.com
        <svg viewBox="0 0 24 24" fill="none" stroke="var(--accent-text)" stroke-width="2"><circle cx="12" cy="12" r="9"/><path d="M3 12h18M12 3c3 3 3 15 0 18M12 3c-3 3-3 15 0 18"/></svg></li>
    </ul>
  </section>

  <section class="card card--back">
    <div class="abs services-pill">OUR SERVICES</div>
    <ul class="abs service-list service-list--main">
      <li>Over Size Loads/Hot Shot Loads</li>
      <li>Heavy Vehicle Recovery Services</li>
      <li>Potable Water Deliveries</li>
      <li>Road Building / Maintenance</li>
      <li>Sand &amp; Metal Supply &amp; Cartage</li>
      <li>Mine Site accredited equipment &amp; Operators</li>
    </ul>
    <ul class="abs service-list service-list--extra">
      <li>Road Train Tippers</li>
      <li>Road Train Tankers</li>
      <li>Road Train Flat Tops</li>
      <li>Drop Deck Trailers</li>
      <li>Earthworks</li>
    </ul>
    <div class="abs truck-photo" role="img" aria-label="White prime mover hauling a grader on a low loader trailer"></div>
    <div class="abs accent-bar"></div>
    <p class="abs pitch">We offer a large range of services not listed.<br>So call us today for a personalised quote to<br>suit your needs.</p>
    <p class="abs depot"><span>Depot:</span> Lot 41, Redgum Flat Road, Marla Creek</p>
  </section>
</main>
</body>
</html>
```